Banner ad for hyper local news site

We need a banner (that we will use on our own site) to explain to people that they can "be the reporter" in their local area. Lanternway is an Australia community news network. We cover local news on a daily basis but also allow people and organisations to publish their own news direct to the site. We are trying to encourage local dialogue and to empower people to talk about the things that matter to them and get their issues on the news agenda.

We need a 'call to action' banner that explains to our users that they can post their own stories on the site.

Some suggested text (thinking this would be rolling)

*Lanternway is YOUR voice in the community
*You can 'be the reporter' and write your own news
*To be heard, contribute your stories, click here - it's free

The banner doesn't have to be slick - we'd prefer a warm and friendly community feeling....but also something in keeping with the look and feel of our site wwww.lanternway-example.com.au

Industry/Entity Type

News

```html
<!DOCTYPE html>
<html lang="en">
<head>
<meta charset="utf-8">
<title>Lanternway – Be the reporter banners</title>
<link rel="stylesheet" href="https://fonts.googleapis.com/css2?family=Source+Sans+3:wght@900&display=swap">
<style>
  :root {
    --backdrop: #9ca894;
    --paper-light: #f3ecd8;
    --paper-mid: #e6d9b8;
    --paper-edge: #cdb98c;
    --frame: #3b3a32;
    --outline: #ffffff;
    --shadow: rgba(40, 30, 15, 0.75);
    --ink-blue: #1d6fd3;
    --ink-green: #14781b;
    --ink-red: #a3121a;
    --ink-olive: #3f7a12;
  }
  html, body {
    margin: 0;
    padding: 0;
    width: 1200px;
    height: 821px;
    overflow: hidden;
    background: var(--backdrop);
  }
  .banner-set {
    position: relative;
    width: 1200px;
    height: 821px;
  }
  .banner {
    position: absolute;
    left: 0;
    width: 1198px;
    height: 138px;
    border: 1px solid var(--frame);
    background:
      radial-gradient(ellipse at 50% 45%, var(--paper-light) 0%, var(--paper-mid) 55%, var(--paper-edge) 100%);
    display: flex;
    align-items: center;
    justify-content: center;
    box-sizing: content-box;
  }
  .banner--blue  { top: 0; }
  .banner--green { top: 206px; }
  .banner--red   { top: 419px; }
  .banner--olive { top: 634px; }

  .banner__headline {
    margin: 0;
    font-family: "Source Sans 3", "Segoe UI", sans-serif;
    font-weight: 900;
    font-size: 96px;
    letter-spacing: -1px;
    line-height: 1;
    white-space: nowrap;
    text-shadow:
      3px 0 0 var(--outline), -3px 0 0 var(--outline),
      0 3px 0 var(--outline), 0 -3px 0 var(--outline),
      2px 2px 0 var(--outline), -2px -2px 0 var(--outline),
      2px -2px 0 var(--outline), -2px 2px 0 var(--outline),
      7px 7px 6px var(--shadow);
  }
  .banner--blue  .banner__headline { color: var(--ink-blue); }
  .banner--green .banner__headline { color: var(--ink-green); }
  .banner--red   .banner__headline { color: var(--ink-red); }
  .banner--olive .banner__headline { color: var(--ink-olive); }
</style>
</head>
<body>
  <main class="banner-set">
    <section class="banner banner--blue">
      <p class="banner__headline">You can&nbsp; 'be the reporter'</p>
    </section>
    <section class="banner banner--green">
      <p class="banner__headline">You can&nbsp; 'be the reporter'</p>
    </section>
    <section class="banner banner--red">
      <p class="banner__headline">You can&nbsp; 'be the reporter'</p>
    </section>
    <section class="banner banner--olive">
      <p class="banner__headline">You can&nbsp; 'be the reporter'</p>
    </section>
  </main>
</body>
</html>
```